Client Fulfillment Flyer

This is a document used for internal purposes ie it is not distributed to clients. We would like it to have some colour, images etc. We are in the financial services industry, Ballarat, Victoria, Australia. www.tarrowfield.com.au and www.tarrowfieldagri.com.au

Target Market(s)

Internal training document

Industry/Entity Type

Finance And Accounting

Colors
3176b5

```html
<!DOCTYPE html>
<html lang="en">
<head>
<meta charset="utf-8">
<title>Tarrowfield &amp; Co Client Fulfillment System</title>
<link rel="stylesheet" href="https://fonts.googleapis.com/css2?family=Lato:wght@400;700&family=Oswald:wght@500&family=Merriweather:wght@400&display=swap">
<style>
:root{
  --navy:#0f4585;
  --blue:#1d5c9f;
  --brand:#3176b5;
  --fold:#0b3466;
  --ink:#2b2b2b;
  --card:#ffffff;
  --page:#f6f6f6;
  --frame:#dadada;
  --tint:#e6f1f9;
  --col-a:#e9eef3;
  --col-b:#dfe1e4;
}
*{box-sizing:border-box;margin:0;padding:0}
html,body{width:1200px;height:1200px;overflow:hidden}
body{background:radial-gradient(ellipse at 50% 40%,#ffffff 0%,#e6e6e6 55%,#c9c9c9 100%);font-family:"Lato",Arial,sans-serif;color:var(--ink);position:relative}
.page{position:absolute;background:var(--page);border:5px solid var(--frame);overflow:hidden}
.page--intro{left:390px;top:16px;width:392px;height:554px}
.page--management{left:162px;top:584px;width:424px;height:598px}
.page--roles{left:630px;top:586px;width:421px;height:596px}
.masthead{height:57px;background:#fff;display:flex;align-items:center;justify-content:space-between;padding:0 12px 0 8px}
.brand{display:flex;align-items:center;gap:9px}
.brand__mark{width:40px;height:40px;border-radius:50%;background:var(--navy)}
.brand__name{font-family:"Lato",sans-serif;font-weight:700;font-size:13px;letter-spacing:1.4px;color:var(--blue);text-transform:uppercase}
.contact{font-size:7.6px;font-weight:700;color:var(--blue);line-height:10px}
.contact div{display:flex;align-items:center;gap:4px}
.contact svg{width:8px;height:8px}
.titleband{background:var(--navy);height:19px;margin:0 -5px;text-align:center;color:#fff;font-family:"Oswald",sans-serif;font-weight:500;font-size:14px;line-height:19px;letter-spacing:-.1px}
.section{position:relative;margin:14px 8px 0}
.ribbon{position:relative;z-index:2;display:table;margin:0 auto -8px;background:var(--blue);color:#fff;font-family:"Merriweather",serif;font-size:11px;line-height:17px;padding:0 14px;box-shadow:0 1px 2px rgba(0,0,0,.25)}
.ribbon::before,.ribbon::after{content:"";position:absolute;top:-5px;border-style:solid;border-color:transparent}
.ribbon::before{left:-6px;border-width:0 0 5px 6px;border-bottom-color:#6f9ccc}
.ribbon::after{right:-6px;border-width:0 6px 5px 0;border-bottom-color:#6f9ccc}
.card{background:var(--card);box-shadow:0 1px 3px rgba(0,0,0,.18);padding:14px 8px 7px;font-size:6.6px;line-height:8.6px}
.card b{font-weight:700}
.card .accent{color:var(--brand)}
.card ul{list-style:none}
.card li::before{content:"\2022";color:var(--brand);margin-right:3px}
.subhead{color:var(--blue);font-weight:700;font-size:7.2px;margin-top:6px}
.lead{color:var(--blue);font-weight:700;font-size:7px}
.negotiables{background:var(--tint);margin:4px -8px -7px;padding:6px 8px 7px 10px}
.negotiables h3{color:var(--brand);font-size:9px;font-weight:700;margin:-2px 0 5px -2px}
.negotiables ol{list-style:none;counter-reset:n}
.negotiables li{counter-increment:n;position:relative;padding-left:26px}
.negotiables li::before{content:counter(n);position:absolute;left:0;top:1px;width:7px;height:7px;border-radius:50%;background:var(--blue);color:#fff;font-size:5px;line-height:7px;text-align:center;font-weight:700;margin:0}
.footband{position:absolute;left:-5px;right:-5px;bottom:-5px;height:29px;background:var(--navy);display:flex;align-items:center;justify-content:flex-end;gap:5px;padding-right:14px}
.footband::before{content:"";position:absolute;left:0;right:95px;top:14px;height:2px;background:var(--blue)}
.footband span{width:17px;height:17px;border-radius:50%;background:#fff}
.roles{margin:20px 8px 0 16px;width:calc(100% - 24px);border-collapse:collapse;font-size:6.6px;line-height:9.1px;table-layout:fixed}
.roles th{font-weight:400;color:#fff;font-size:7px;line-height:8px;height:26px;vertical-align:middle;border-left:2px solid var(--page)}
.roles th.col-csm{background:#5b9bd3}
.roles th.col-manila{background:#3c74ad}
.roles th.col-acc{background:var(--blue)}
.roles th.col-partner{background:var(--navy)}
.roles td{vertical-align:top;border-left:2px solid var(--page);text-align:center;color:var(--brand);font-weight:700}
.roles td.task{text-align:left;color:var(--ink);font-weight:400;border-left:none;padding-left:7px;text-indent:-6px}
.roles td.task::before{content:"\2022";color:var(--brand);margin-right:3px}
.roles td.c1,.roles td.c3{background:var(--col-a)}
.roles td.c2,.roles td.c4{background:var(--col-b)}
.roles tr.first td{padding-top:8px}
</style>
</head>
<body>

<section class="page page--intro">
  <header class="masthead">
    <div class="brand"><div class="brand__mark"></div><div class="brand__name">Tarrowfield &amp; Co</div></div>
    <div class="contact">
      <div><svg viewBox="0 0 10 10"><path d="M2 1l2 2-1 1.3c.6 1.2 1.5 2.1 2.7 2.7L7 6l2 2-1.2 1.2C4.5 9 1 5.5.8 2.2z" fill="#1d5c9f"/></svg>(03) 5550 0142</div>
      <div><svg viewBox="0 0 10 10"><rect x="1" y="2" width="8" height="6" fill="none" stroke="#1d5c9f"/><path d="M1 2l4 3 4-3" fill="none" stroke="#1d5c9f"/></svg>info@tarrowfieldagri.com.au</div>
    </div>
  </header>
  <h1 class="titleband">THE TARROWFIELD &amp; CO CLIENT FULFILLMENT SYSTEM</h1>

  <div class="section">
    <h2 class="ribbon">Client Fulfillment</h2>
    <div class="card">
      We are primarily a service based business however the product we sell is <b>Client Fulfillment.</b><br>
      Client Fulfillment in simple terms means <span class="accent">providing the services to satisfy client requirements and expectations.</span><br>
      Our aim is to not only satisfy but exceed client requirements and expectations.<br>
      The Client Fulfillment system is the methodology through which we deliver the result we have promised to deliver.<br>
      <b>Why is this important?</b> In order to achieve our Core Purpose and Vision, delivering Client Fulfillment is essential.
    </div>
  </div>

  <div class="section">
    <h2 class="ribbon">The Client Fulfillment Process</h2>
    <div class="card">
      <b>The areas we focus on to deliver Client Fulfillment are:</b>
      <ul>
        <li>Understanding Core Purpose, Core Values, Vision and Why</li>
        <li>Client Management and Communication</li>
        <li>The Basics</li>
        <li>The Are You Financially Secure Process</li>
        <li>The Right People Doing the Right Work</li>
      </ul>
    </div>
  </div>

  <div class="section">
    <h2 class="ribbon">Understanding Core Purpose, Core Values, Vision and Why</h2>
    <div class="card">
      These terms can be overwhelming and confusing but to deliver Client Fulfillment it is important to understand what it all means and how it all connects. Our Core Purpose and Core Values are the foundation of our business. We have a clear Vision of where we want the business to go, that is what does it look like in 10 years. Underlying this is our <b>WHY.</b> We know what we do and how to do it, but more importantly is WHY we do it and what drives us each day to help our clients.
      <p class="subhead">Our Vision. What is it?</p>
      This is our Vision across the entire Tarrowfield &amp; Co business:<br>
      <b>To provide all businesses and individuals with the opportunity to achieve financial security.</b><br>
      Our business is designed so people can access all the services required to achieve financial security.<br>
      We are a motivated team that embraces change and technology along with having the knowledge, skills and expertise to help committed clients achieve financial security.<br>
      We believe everyone deserves this opportunity and we are committed to proactively engage with existing and future clients to share and demonstrate the positive impact we can make to their lives.<br>
      We do not limit the number of people we can help and distance is not a barrier.<br>
      Our goal by 30th June 2023 is to be helping at least 5,000 client/family groups along their journey to reach the financial goals and dreams they are committed to achieving.
      <p class="subhead">How are we going to achieve our Vision?</p>
      We need to work in an <b>effective and efficient manner</b> to achieve this vision.<br>
      We break the vision down into smaller plans and action items. We then prioritise these steps with responsibility and accountability around each step to be completed.<br>
      As each step is in progress and being completed we are getting closer to achieving our vision. For example the implementation of Ledgerly, Manila and client allocations are all important steps towards achieving our vision.
    </div>
  </div>

  <footer class="footband"><span></span><span></span><span></span></footer>
</section>

<section class="page page--management">
  <header class="masthead">
    <div class="brand"><div class="brand__mark"></div><div class="brand__name">Tarrowfield &amp; Co</div></div>
    <div class="contact">
      <div><svg viewBox="0 0 10 10"><path d="M2 1l2 2-1 1.3c.6 1.2 1.5 2.1 2.7 2.7L7 6l2 2-1.2 1.2C4.5 9 1 5.5.8 2.2z" fill="#1d5c9f"/></svg>(03) 5550 0142</div>
      <div><svg viewBox="0 0 10 10"><rect x="1" y="2" width="8" height="6" fill="none" stroke="#1d5c9f"/><path d="M1 2l4 3 4-3" fill="none" stroke="#1d5c9f"/></svg>info@tarrowfieldagri.com.au</div>
    </div>
  </header>
  <h1 class="titleband">THE TARROWFIELD &amp; CO CLIENT FULFILLMENT SYSTEM</h1>

  <div class="section" style="margin-top:10px">
    <div class="card" style="padding-top:6px">
      <p class="lead">We also have a clearly defined Core Purpose, Core Values, and Why – Why we do what we do.</p>
      Our core purpose states the reason we exist. The core values are our fundamental beliefs of how we go about our work on a daily basis. Our Core Purpose and Values stay the same irrespective of how our business changes.<br>
      Understanding our Why helps to provide a connection with our vision and purpose. Rather than focusing on what we do and how we do it, we need to understand why we do it.<br>
      If you understand WHY, it gives a greater purpose to the work you do every day. It's a mindset – are you at work to process transactions and lodge tax returns or are you here completing an important step in identifying ways to help committed clients achieve financial security?<br>
      The latter mindset will not only ensure you are doing what is required but more importantly help you personally find fulfilment in your role.<br>
      We have Service Standards and Culture Standards. These are the basic rules and expectations of how all team members work and interact.
    </div>
  </div>

  <div class="section">
    <h2 class="ribbon" style="font-size:11.5px">Client Management and Communication</h2>
    <div class="card">
      Client Management and Communication in the context of delivering Client Fulfillment is understanding our client needs, requirements and expectations and ensuring the delivery is in a manner consistent with our Core Purpose and Core Values whilst achieving our Vision.<br>
      This means to deliver Client Fulfillment and achieve our vision we must plan, organise and execute in a consistent manner so there is a reliable and consistent outcome for our clients.<br>
      People like to feel valued and not just a small part of a big business. Utilising our CRM and technology means that we can reach out to individuals with relevant information to help forge and maintain relationships.<br>
      Having the right people doing the right work as well as following the required systems and processes will ensure there is adequate time to invest in Client Management and Communication.
      <div class="negotiables">
        <h3>The 10 Non Negotiables:</h3>
        <ol>
          <li>Client phone calls and emails are replied to the same day received. Even if to say, received call/email will respond .... OR have CSM contact client on your behalf.</li>
          <li>Work is allocated / delegated to the appropriate team member.</li>
          <li>Systems, processes and checklists are used.</li>
          <li>All compliance work and lodgments are completed on time and by due dates.</li>
          <li>A fee proposal is communicated to client before starting work if it is not already covered by the annual fee agreement.</li>
          <li>The AYFS requirements are completed and updated annually (normally with Annual Accounts meeting).</li>
          <li>Annual Accounts meeting occurs once annual financial statements and taxation returns are completed.</li>
          <li>There is a minimum of monthly communication to clients under management.</li>
          <li>Prior to going on leave client work is planned and necessary arrangements are put in place to ensure clients under management are being looked after. This includes an automated email response as follows:<br>Thank you for your email.<br>I am currently on leave until ENTER DATE. I may not have email access whilst away so please contact the following team members for assistance.<br>ACCOUNTANT NAME &amp; EMAIL ADDRESS, CSM NAME &amp; EMAIL ADDRESS</li>
          <li>We are outcome focused rather than timesheet focused.</li>
        </ol>
      </div>
    </div>
  </div>

  <footer class="footband"><span></span><span></span><span></span></footer>
</section>

<section class="page page--roles">
  <header class="masthead">
    <div class="brand"><div class="brand__mark"></div><div class="brand__name">Tarrowfield &amp; Co</div></div>
    <div class="contact">
      <div><svg viewBox="0 0 10 10"><path d="M2 1l2 2-1 1.3c.6 1.2 1.5 2.1 2.7 2.7L7 6l2 2-1.2 1.2C4.5 9 1 5.5.8 2.2z" fill="#1d5c9f"/></svg>(03) 5550 0142</div>
      <div><svg viewBox="0 0 10 10"><rect x="1" y="2" width="8" height="6" fill="none" stroke="#1d5c9f"/><path d="M1 2l4 3 4-3" fill="none" stroke="#1d5c9f"/></svg>info@tarrowfieldagri.com.au</div>
    </div>
  </header>
  <h1 class="titleband">THE TARROWFIELD &amp; CO CLIENT FULFILLMENT SYSTEM</h1>

  <div class="section">
    <h2 class="ribbon" style="font-size:12px">The Right People Doing The Right Work</h2>
    <div class="card">
      A team is a group of individuals all working together for a common purpose. Each team member has a role in the team to achieve the goal or result. To deliver Client Fulfillment it is important that we work as a team and understand our role and the tasks attached to that role. This will ensure as a team we are directing our time and focus in the way required to have the capacity to deliver Client Fulfillment. Much of our time is invested completing The Basics. However on a daily basis there is so much more to do to help clients and having the capacity to complete this additional work is vital to delivering Client Fulfillment.<br>
      Below is a table of the many jobs and tasks we do on a daily basis and the team member role that is responsible for that task.
    </div>
  </div>

  <table class="roles">
    <colgroup><col style="width:178px"><col><col><col><col></colgroup>
    <thead>
      <tr><th></th><th class="col-csm">CSM</th><th class="col-manila">Manila<br>Accountant</th><th class="col-acc">Accountant</th><th class="col-partner">Senior Mgr.<br>Partner</th></tr>
    </thead>
    <tbody>
      <tr class="first"><td class="task">Contacting clients for missing information</td><td class="c1">✓</td><td class="c2"></td><td class="c3"></td><td class="c4"></td></tr>
      <tr><td class="task">Changes to database / CRM</td><td class="c1">✓</td><td class="c2"></td><td class="c3"></td><td class="c4"></td></tr>
      <tr><td class="task">Returning client records</td><td class="c1">✓</td><td class="c2"></td><td class="c3"></td><td class="c4"></td></tr>
      <tr><td class="task">Preparing Balance Date Checklists</td><td class="c1">✓</td><td class="c2"></td><td class="c3"></td><td class="c4"></td></tr>
      <tr><td class="task">Fee proposal draft preparation and send to client once final</td><td class="c1">✓</td><td class="c2"></td><td class="c3"></td><td class="c4"></td></tr>
      <tr><td class="task">Job set up</td><td class="c1">✓</td><td class="c2"></td><td class="c3"></td><td class="c4"></td></tr>
      <tr><td class="task">Confirm fee proposal details, explain benefit to client and value</td><td class="c1"></td><td class="c2"></td><td class="c3">✓</td><td class="c4">✓</td></tr>
      <tr><td class="task">Setting Due Dates for all jobs in workflow program</td><td class="c1">✓</td><td class="c2"></td><td class="c3"></td><td class="c4"></td></tr>
      <tr><td class="task">Collating information to send to banks, finance co's etc, and sending once confirmed</td><td class="c1">✓</td><td class="c2"></td><td class="c3"></td><td class="c4"></td></tr>
      <tr><td class="task">Setting and managing Start Dates and To-do Dates in workflow program</td><td class="c1"></td><td class="c2"></td><td class="c3">✓</td><td class="c4"></td></tr>
      <tr><td class="task">Manage workflow to meet client expectations and team sales budget</td><td class="c1"></td><td class="c2"></td><td class="c3">✓</td><td class="c4">✓</td></tr>
      <tr><td class="task">Communicate workflow concerns and bottlenecks before they become an issue</td><td class="c1"></td><td class="c2"></td><td class="c3">✓</td><td class="c4"></td></tr>
      <tr><td class="task">Dealing with Tax Office correspondence</td><td class="c1">✓</td><td class="c2"></td><td class="c3"></td><td class="c4"></td></tr>
      <tr><td class="task">Contacting the Tax Office</td><td class="c1">✓</td><td class="c2"></td><td class="c3"></td><td class="c4"></td></tr>
      <tr><td class="task">Advising clients of PAYG instalment amounts and due dates</td><td class="c1">✓</td><td class="c2"></td><td class="c3"></td><td class="c4"></td></tr>
      <tr><td class="task">Printing, binding financial statements, tax returns and reports etc</td><td class="c1">✓</td><td class="c2"></td><td class="c3"></td><td class="c4"></td></tr>
      <tr><td class="task">Advising clients of TFN, ABN, GST registrations etc</td><td class="c1">✓</td><td class="c2"></td><td class="c3"></td><td class="c4"></td></tr>
      <tr><td class="task">Advising clients of tax assessment notices</td><td class="c1">✓</td><td class="c2"></td><td class="c3"></td><td class="c4"></td></tr>
      <tr><td class="task">Invoicing and job completion</td><td class="c1">✓</td><td class="c2"></td><td class="c3"></td><td class="c4"></td></tr>
      <tr><td class="task">Monitoring Activity Statement lodgments</td><td class="c1">✓</td><td class="c2"></td><td class="c3"></td><td class="c4"></td></tr>
      <tr><td class="task">Manage new entity set ups</td><td class="c1">✓</td><td class="c2"></td><td class="c3"></td><td class="c4"></td></tr>
      <tr><td class="task">Monitor Tax Office lodgment and payment dates</td><td class="c1">✓</td><td class="c2"></td><td class="c3"></td><td class="c4"></td></tr>
    </tbody>
  </table>

  <footer class="footband"><span></span><span></span><span></span></footer>
</section>

</body>
</html>
```